A new web site design for Velbrona.com

Create a new clean and modern design for Velbrona.com. This site will be a straight HTML site that will feature videos, PDF downloads, contact us page and marketing capture forms in front of some of the downloadable content. Quillbase hub is an example of a related product and an example of what we consider a good design ( https://www.quillbasehub.example/ ) We are open to any design and colours schemes however we have an existing logo. I have also attached a PDF brochure design that we had built before for reference, and a word document with the menu structure and some initial content.
Target Market(s)
CIO of large corporations
Industry/Entity Type
Saas
Coding
Coded - Design and coding required
Number of Pages Required
5+ page
Font styles to use
Look and feel
Each slider illustrates characteristics of the customer's brand and the style your logo design should communicate.

```html
<!DOCTYPE html>
<html lang="en">
<head>
<meta charset="utf-8">
<title>Velbrona – TBM Run Model</title>
<link href="https://fonts.googleapis.com/css2?family=Cinzel:wght@600;700&family=Montserrat:wght@500;600&family=Mulish:wght@400;600&display=swap" rel="stylesheet">
<style>
:root{
  --navy:#161f57;
  --navy-deep:#131b4c;
  --orange:#ff6a00;
  --blue-box:#3aa2f2;
  --text:#3c3c3c;
  --muted:#8a8a8a;
  --rule:#e2e2e2;
  --white:#ffffff;
  --hero-a:#8fb1d8;
  --hero-b:#c9dcf0;
}
*{box-sizing:border-box;margin:0;padding:0}
html,body{width:1200px;height:2242px;overflow:hidden;background:var(--white)}
body{position:relative;font-family:"Mulish",Arial,sans-serif;color:var(--text)}
.abs{position:absolute}

.topbar{left:0;top:0;width:1200px;height:45px;background:var(--navy)}
.topbar-contact{right:78px;top:13px;display:flex;gap:22px;color:var(--white);font:500 14px "Montserrat",Arial,sans-serif}
.topbar-contact span{display:flex;align-items:center;gap:8px}

.header{left:0;top:45px;width:1200px;height:105px;background:var(--white);border-bottom:1px solid var(--rule)}
.brand{left:88px;top:38px;display:flex;align-items:center;gap:12px;color:var(--navy);font:600 27px "Cinzel",Georgia,serif;letter-spacing:3px}
.brand-mark{width:16px;height:16px;background:var(--navy)}
.nav{right:72px;top:64px;display:flex;align-items:center;font:500 13px "Montserrat",Arial,sans-serif;color:#222}
.nav a{color:inherit;text-decoration:none;padding:0 27px;border-left:1px solid #d8d8d8;line-height:16px}
.nav a:first-child{border-left:0}
.nav a.active{color:var(--navy)}

.hero{left:0;top:150px;width:1200px;height:387px;background:linear-gradient(100deg,var(--hero-a),var(--hero-b))}

.section-title{left:0;width:1200px;text-align:center;color:var(--navy);font:700 34px "Cinzel",Georgia,serif}
.title-rule{left:520px;width:160px;height:1px;background:#d0d0d0}
.title-rule-dot{left:595px;width:10px;height:10px;border:1px solid #c0c0c0;background:var(--white);transform:rotate(45deg)}
.lead{left:90px;width:1020px;text-align:center;font-size:15px;line-height:26px;color:var(--text)}
.sub-title{left:0;width:1200px;text-align:center;color:#111;font:600 21px "Montserrat",Arial,sans-serif}
.footnote{left:0;width:1200px;text-align:center;font-size:15px;color:var(--muted)}
.divider{left:0;top:1416px;width:1200px;height:2px;background:var(--rule)}

.pie{left:0;top:850px}
.pie text{font:600 16px "Montserrat",Arial,sans-serif;fill:#111}

.fw-box{left:84px;height:33px;background:var(--blue-box);color:var(--white);font-size:12px;display:flex;align-items:center;justify-content:center;border-radius:2px}
.fw-lines{left:84px;top:1524px}
.fw-text{left:494px;top:1524px;width:620px;font-size:15px;line-height:26px}
.fw-text p{margin-bottom:16px}
.download{left:494px;top:1763px;width:272px;height:49px;background:var(--navy);color:var(--white);font:600 15px "Montserrat",Arial,sans-serif;display:flex;align-items:center;justify-content:center;gap:12px;clip-path:polygon(12px 0,260px 0,272px 24px,260px 49px,12px 49px,0 24px)}

.footer{left:0;top:1875px;width:1200px;height:314px;background:var(--navy-deep);color:#d8dbea}
.footer-head{font:600 18px "Cinzel",Georgia,serif;color:var(--white);letter-spacing:1px;padding-bottom:12px;border-bottom:1px solid #2e3870;width:228px}
.footer-head em{font-style:normal;color:var(--orange)}
.links{left:81px;top:45px}
.links ul{list-style:none;margin-top:16px;font-size:14px}
.links li{line-height:31px}
.links li::before{content:"•";margin-right:8px}
.links li.current{color:var(--orange)}
.contact{left:345px;top:45px;font-size:14px;line-height:22px}
.contact strong{display:block;margin-top:16px;color:var(--white);font:600 15px "Montserrat",Arial,sans-serif}
.contact .row{display:flex;align-items:center;gap:12px;margin-top:9px}
.inquiry{left:647px;top:45px}
.inquiry .field{width:266px;height:34px;background:var(--white);margin-top:8px;font-size:12px;color:#aaa;padding:10px 10px}
.inquiry .field:first-of-type{margin-top:18px}
.submit{width:124px;height:34px;background:var(--orange);color:var(--white);font:600 15px "Montserrat",Arial,sans-serif;display:flex;align-items:center;justify-content:center;margin-top:9px;border:1px solid #ffb070}
.footer-name{left:960px;top:125px;color:#3e4781;font:700 38px "Cinzel",Georgia,serif;letter-spacing:2px}

.bottombar{left:0;top:2189px;width:1200px;height:53px;background:var(--orange)}
.copyright{left:81px;top:19px;color:var(--white);font:500 12px "Montserrat",Arial,sans-serif}
.social{right:77px;top:11px;display:flex;gap:7px}
.social span{width:31px;height:31px;border-radius:50%;background:var(--navy);border:2px solid var(--white)}
</style>
</head>
<body>

<div class="abs topbar">
  <div class="abs topbar-contact">
    <span><svg width="13" height="13" viewBox="0 0 24 24"><path fill="#fff" d="M6.6 10.8a15 15 0 0 0 6.6 6.6l2.2-2.2c.3-.3.7-.4 1-.2 1.1.4 2.3.6 3.6.6.6 0 1 .4 1 1V20c0 .6-.4 1-1 1A17 17 0 0 1 3 4c0-.6.4-1 1-1h3.5c.6 0 1 .4 1 1 0 1.3.2 2.5.6 3.6.1.3 0 .7-.2 1z"/></svg>(123) 456 7890</span>
    <span><svg width="13" height="13" viewBox="0 0 24 24"><path fill="#fff" d="M2 11 22 2l-9 20-2-9z"/></svg>info@velbrona.com</span>
  </div>
</div>

<header class="abs header">
  <div class="abs brand"><span class="brand-mark"></span>VELBRONA</div>
  <nav class="abs nav">
    <a href="#">HOME</a>
    <a href="#" class="active">MODEL EXAMPLE</a>
    <a href="#">RESOURCES &#9662;</a>
    <a href="#">PRICING</a>
    <a href="#">ABOUT US</a>
    <a href="#">CONTACT US</a>
  </nav>
</header>

<div class="abs hero" role="img" aria-label="Illustration of a desktop monitor, laptop, tablet and phone showing analytics charts"></div>

<h1 class="abs section-title" style="top:585px">TBM RUN</h1>
<div class="abs title-rule" style="top:644px"></div>
<div class="abs title-rule-dot" style="top:639px"></div>

<p class="abs lead" style="top:670px">IT Run Model 1 is a simple IT costing model suitable for any industry.&nbsp; It is designed to support a sophisticated level of cost transparency across common IT technologies, towers and services with a minimum of effort.&nbsp; As a starting point this model is mainly focused on the IT costs that run the business.&nbsp; However, it can be extended to cover a detailed view of IT investments that change the business as well. In addition, it can be used as a starting point to manage demand by extending support for specific business processes.</p>

<h2 class="abs sub-title" style="top:801px">Tech Towers (Run Build Manage)</h2>

<svg class="abs pie" width="1200" height="360" viewBox="0 0 1200 360">
  <g transform="translate(610 203) scale(1 0.6) rotate(-150)" fill="none" stroke-width="102">
    <g transform="translate(0 0)">
    </g>
  </g>
  <!-- depth layer -->
  <g transform="translate(610 228) scale(1 0.6) rotate(-150)" fill="none" stroke-width="102">
    <circle r="86" pathLength="100" stroke="#4a4a86" stroke-dasharray="27 73" stroke-dashoffset="0"/>
    <circle r="86" pathLength="100" stroke="#7a0e80" stroke-dasharray="17 83" stroke-dashoffset="-27"/>
    <circle r="86" pathLength="100" stroke="#1c9c80" stroke-dasharray="12 88" stroke-dashoffset="-44"/>
    <circle r="86" pathLength="100" stroke="#b08a18" stroke-dasharray="26 74" stroke-dashoffset="-56"/>
    <circle r="86" pathLength="100" stroke="#3f6b6a" stroke-dasharray="12 88" stroke-dashoffset="-82"/>
    <circle r="86" pathLength="100" stroke="#10709c" stroke-dasharray="6 94" stroke-dashoffset="-94"/>
  </g>
  <g transform="translate(610 216) scale(1 0.6) rotate(-150)" fill="none" stroke-width="102">
    <circle r="86" pathLength="100" stroke="#4a4a86" stroke-dasharray="27 73" stroke-dashoffset="0"/>
    <circle r="86" pathLength="100" stroke="#7a0e80" stroke-dasharray="17 83" stroke-dashoffset="-27"/>
    <circle r="86" pathLength="100" stroke="#1c9c80" stroke-dasharray="12 88" stroke-dashoffset="-44"/>
    <circle r="86" pathLength="100" stroke="#b08a18" stroke-dasharray="26 74" stroke-dashoffset="-56"/>
    <circle r="86" pathLength="100" stroke="#3f6b6a" stroke-dasharray="12 88" stroke-dashoffset="-82"/>
    <circle r="86" pathLength="100" stroke="#10709c" stroke-dasharray="6 94" stroke-dashoffset="-94"/>
  </g>
  <g transform="translate(610 203) scale(1 0.6) rotate(-150)" fill="none" stroke-width="102">
    <circle r="86" pathLength="100" stroke="#6966ac" stroke-dasharray="27 73" stroke-dashoffset="0"/>
    <circle r="86" pathLength="100" stroke="#b004b0" stroke-dasharray="17 83" stroke-dashoffset="-27"/>
    <circle r="86" pathLength="100" stroke="#33f7c9" stroke-dasharray="12 88" stroke-dashoffset="-44"/>
    <circle r="86" pathLength="100" stroke="#ffcc2e" stroke-dasharray="26 74" stroke-dashoffset="-56"/>
    <circle r="86" pathLength="100" stroke="#6b9c9a" stroke-dasharray="12 88" stroke-dashoffset="-82"/>
    <circle r="86" pathLength="100" stroke="#1ba2dc" stroke-dasharray="6 94" stroke-dashoffset="-94"/>
  </g>
  <ellipse cx="610" cy="206" rx="35" ry="20" fill="#ffffff"/>

  <g stroke="#666" stroke-width="1">
    <line x1="556" y1="46" x2="556" y2="80"/>
    <line x1="742" y1="109" x2="706" y2="109"/>
    <line x1="436" y1="147" x2="478" y2="147"/>
    <line x1="787" y1="200" x2="745" y2="200"/>
    <line x1="430" y1="206" x2="468" y2="206"/>
    <line x1="610" y1="320" x2="610" y2="290"/>
  </g>
  <circle cx="556" cy="46" r="3" fill="#6966ac"/>
  <circle cx="742" cy="109" r="3" fill="#b004b0"/>
  <circle cx="436" cy="147" r="3" fill="#1ba2dc"/>
  <circle cx="787" cy="200" r="3" fill="#1c6b5a"/>
  <circle cx="430" cy="206" r="3" fill="#333"/>
  <circle cx="610" cy="320" r="3" fill="#e0a81a"/>

  <text x="556" y="27" text-anchor="middle">Networks &amp; Telecoms</text>
  <text x="777" y="115">End User Computing</text>
  <text x="420" y="153" text-anchor="end">Not Allocated</text>
  <text x="802" y="206">Datacenter &amp; Servers</text>
  <text x="415" y="212" text-anchor="end">Helpdesk &amp; Ops Bridge</text>
  <text x="610" y="348" text-anchor="middle">Apps Maintenace</text>
</svg>

<p class="abs lead" style="top:1239px">The model is a concrete implementation of the Technology Business Management (TBM) * standard framework.&nbsp; TBM has three main views a Finance View, an IT View and a Business view. This model implements these views through three simple layers, IT Cost centres, IT Technology Towers and Products and Services.&nbsp; You can start by implementing just the IT Cost Centres to get some valuable insights before moving on to the IT Towers and Product/Services layers.</p>
<p class="abs footnote" style="top:1358px">*For Technology Business Management (TBM) see tbmforum.example</p>

<div class="abs divider"></div>

<h2 class="abs sub-title" style="top:1459px">Technology Business Management (TBM) Framework</h2>

<svg class="abs fw-lines" width="364" height="300" viewBox="0 0 364 300">
  <g stroke="#333" stroke-width="1" fill="none">
    <line x1="77" y1="72" x2="77" y2="46"/>
    <line x1="282" y1="72" x2="282" y2="46"/>
    <line x1="182" y1="134" x2="182" y2="116"/>
    <line x1="142" y1="116" x2="222" y2="116"/>
    <line x1="142" y1="116" x2="142" y2="107"/>
    <line x1="222" y1="116" x2="222" y2="107"/>
    <line x1="182" y1="196" x2="182" y2="167"/>
    <line x1="182" y1="254" x2="182" y2="229"/>
  </g>
  <g fill="#333">
    <path d="M77 40l-4 7h8z"/>
    <path d="M282 40l-4 7h8z"/>
    <path d="M142 102l-4 7h8z"/>
    <path d="M222 102l-4 7h8z"/>
  </g>
</svg>
<div class="abs fw-box" style="top:1530px;width:364px">Business Units</div>
<div class="abs fw-box" style="top:1596px;width:161px">Products</div>
<div class="abs fw-box" style="top:1596px;left:285px;width:163px">Services</div>
<div class="abs fw-box" style="top:1658px;width:364px">Technology Towers</div>
<div class="abs fw-box" style="top:1720px;width:364px">Cost Pools: Standardised Costs</div>
<div class="abs fw-box" style="top:1778px;width:364px">Finance Layer: General Ledger Costs</div>

<div class="abs fw-text">
  <p>A framework like TBM provides a simple but clear way to describe all costs and how they build to technologies, services and applications.</p>
  <p>The cost reference point is the general ledger meaning clear reconciliation with corporate financial systems.</p>
  <p>The next page details the model layers and categories. It splits costs over three broad categories: Build, Manage and Run. In TBM terminology Run is IT that supports the existing business while Build is equivalent to change the business.</p>
</div>
<a class="abs download" href="#"><svg width="24" height="22" viewBox="0 0 24 22"><path fill="#fff" d="M10 0h4v10h4l-6 7-6-7h4z"/><path fill="#fff" d="M0 13h3v6h18v-6h3v9H0z"/></svg>Download The Full Model</a>

<footer class="abs footer">
  <div class="abs links">
    <div class="footer-head" style="width:195px">Quick <em>Links</em></div>
    <ul>
      <li>Home</li>
      <li class="current">Model Example</li>
      <li>Resources</li>
      <li>Pricing</li>
      <li>About Us</li>
      <li>Contact Us</li>
    </ul>
  </div>
  <div class="abs contact">
    <div class="footer-head">Contact <em>Details</em></div>
    <strong>VELBRONA</strong>
    123, Ut wisi enim ad minim veniam,<br>Mor nostri tation -123 456
    <div class="row" style="margin-top:14px"><svg width="14" height="14" viewBox="0 0 24 24"><path fill="#ff6a00" d="M6.6 10.8a15 15 0 0 0 6.6 6.6l2.2-2.2c.3-.3.7-.4 1-.2 1.1.4 2.3.6 3.6.6.6 0 1 .4 1 1V20c0 .6-.4 1-1 1A17 17 0 0 1 3 4c0-.6.4-1 1-1h3.5c.6 0 1 .4 1 1 0 1.3.2 2.5.6 3.6.1.3 0 .7-.2 1z"/></svg>(123) 456 7890</div>
    <div class="row" style="margin-top:14px"><svg width="14" height="14" viewBox="0 0 24 24"><rect x="6" y="2" width="12" height="6" fill="#ff6a00"/><rect x="2" y="9" width="20" height="9" fill="#ff6a00"/><rect x="6" y="15" width="12" height="7" fill="#ff6a00"/></svg>(123) 456 7890</div>
    <div class="row" style="margin-top:14px"><svg width="14" height="11" viewBox="0 0 24 18"><rect width="24" height="18" fill="#ff6a00"/><path d="M1 1l11 9 11-9" stroke="#131b4c" stroke-width="2" fill="none"/></svg>info@velbrona.com</div>
  </div>
  <div class="abs inquiry">
    <div class="footer-head" style="width:266px">Quick <em>Inquiry</em></div>
    <div class="field">Name</div>
    <div class="field">Email</div>
    <div class="field">Message</div>
    <div class="submit">Submit</div>
  </div>
  <div class="abs footer-name">VELBRONA</div>
</footer>

<div class="abs bottombar">
  <div class="abs copyright">Copyright 2017 VELBRONA. All rights reserved.</div>
  <div class="abs social"><span></span><span></span><span></span><span></span></div>
</div>

</body>
</html>
```